3-4 Page Research Report Template

We want a template in MS Word that we can use to write up research reports. We want a similar feal as our newsletter and website - but we also want it to look more modern, yet stay in the financial service / investment research world.

Examples: http://media.brelvox.example/Documents/Asset_Allocation_Focus_March2013.pdf

http://www.taskirel.example/Home/Documents/Default.aspx?fileId=58082

Our website: www.hurmontadvisors.example
Our Newsletter: http://www.hurmontadvisors.example/DawlinBrief/2012/2012-11-12.pdf

We want 3 template pages - a cover or 1st page, a middle page and and last or end page.

Reason: I would like more than two designers to compare ideas. I was hoping for 5. This is designers not designs.

We are not looking for a new version of our Newsletter "The Dawlin Brief" - We want a template to publish other research articles. We shared The Dawlin Brief file to give you a better idea on what we currently like / use - though dated as it was designed in 2004. 

That doesn't mean we wont pick a template using The Dawlin Brief as example content. I just wanted to be clear. 

Target Market(s)

Sophisticated investors with over $1M in the market and investment professionals (financial advisors)

Industry/Entity Type

Investment

Requirements
Must have
• Space for disclosures at the end.
Ability to drop in tables and charts/graphs
Should not have
• Do not use the HMRA website masthead directly. Please be creative in helping is get a more modern and fresh design. I provided it as reference on what we already like (or did in 2004 when it was designed).

```html
<!DOCTYPE html>
<html lang="en">
<head>
<meta charset="utf-8">
<title>Research Report – Inner Page</title>
<link href="https://fonts.googleapis.com/css2?family=PT+Sans:wght@400;700&display=swap" rel="stylesheet">
<style>
  :root{
    --brand-blue:#1c4f93;
    --heading-blue:#1f5aa8;
    --band-grey:#8d8f92;
    --band-grey-dark:#7d7f82;
    --text:#2a2a2a;
    --paper:#ffffff;
    --rule-dark:#1b2f4f;
  }
  *{box-sizing:border-box;margin:0;padding:0}
  html,body{width:849px;height:1200px;overflow:hidden;background:var(--paper)}
  .page{position:relative;width:849px;height:1200px;background:var(--paper);
        font-family:"PT Sans",Arial,sans-serif;color:var(--text);overflow:hidden}

  .chapter-header{position:absolute;top:24px;left:51px;right:0;height:84px;display:flex}
  .chapter-number{width:104px;height:100%;background:var(--brand-blue);color:#fff;
        font-weight:700;font-size:46px;line-height:84px;padding-left:12px;position:relative}
  .chapter-number svg{position:absolute;right:4px;bottom:6px}
  .chapter-title-band{flex:1;background:linear-gradient(90deg,var(--band-grey) 0%,var(--band-grey-dark) 100%);
        color:#fff;font-weight:700;font-size:44px;line-height:84px;padding-left:14px;letter-spacing:.5px}

  .side-texture{position:absolute;top:120px;right:0;width:230px;height:980px;
        background:radial-gradient(ellipse at 100% 50%,rgba(150,160,175,.10) 0%,rgba(150,160,175,0) 70%)}

  .body-copy{position:absolute;top:162px;left:51px;width:756px}
  .body-copy h2{color:var(--heading-blue);font-size:16.5px;font-weight:700;line-height:20px}
  .body-copy p{font-size:15px;line-height:20px;margin-bottom:20px}
  .body-copy h2 + p{margin-top:0}

  .page-footer{position:absolute;left:0;right:0;bottom:0;height:74px}
  .page-tab{position:absolute;left:0;top:0;width:196px;height:40px;background:var(--brand-blue);
        color:#fff;font-size:13px;line-height:40px;padding-left:51px}
  .footer-rule{position:absolute;left:0;right:0;top:40px;height:4px;background:var(--rule-dark)}
</style>
</head>
<body>
<div class="page">
  <header class="chapter-header">
    <div class="chapter-number">01.
      <svg width="18" height="18" viewBox="0 0 18 18" aria-hidden="true"><path d="M2 16 L16 2 M7 2 H16 V11" stroke="#fff" stroke-width="2.5" fill="none"/></svg>
    </div>
    <div class="chapter-title-band">TITLE OF THE CHAPTER</div>
  </header>

  <div class="side-texture" role="img" aria-label="Faint concentric arc texture"></div>

  <main class="body-copy">
    <h2>Lorem ipsum dolor sit amet</h2>
    <p>Lorem ipsum dolor sit amet, consectetur adipiscing elit. Morbi euismod sem eget neque consectetur a ultrices nunc porta. Pellentesque pharetra, lacus pharetra vehicula consequat, neque est luctus mauris, at lobortis mauris elit ac felis. Vestibulum blandit nulla at massa lacinia suscipit. Etiam aliquet nisl orci, at congue odio. Nunc vitae lectus mi. Suspendisse blandit consequat mi. Phasellus luctus lacinia lorem fermentum eleifend. Vivamus dignissim sollicitudin turpis et sagittis. Vivamus est dui, scelerisque eget sollicitudin at, lacinia ut ipsum. Aliquam quis sollicitudin arcu.</p>
    <p>Sed volutpat tortor eget quam vulputate elementum. Quisque quis nulla et purus ornare luctus viverra quis est. In eu nunc et mi faucibus varius. Suspendisse et nulla urna. Nunc consequat arcu ipsum. Donec vel purus tortor. Donec ac urna arcu, ut scelerisque lacus. Morbi lacus enim, scelerisque sit amet tempus nec, pharetra et mauris. Quisque a lectus turpis. Vivamus velit nisi, vestibulum in viverra eu, sodales vestibulum quam. Maecenas neque lorem, malesuada et tempus nec, tempor nec nisl.</p>
    <h2>Lorem ipsum dolor sit amet</h2>
    <p>Nam dui tortor, bibendum vel egestas at, vulputate a augue. Etiam a augue auctor libero consectetur fermentum. Cras vitae erat ac nisi faucibus tempor ac sit amet urna. Curabitur fringilla aliquam magna vel tempus. In sodales dui quis lacus pellentesque euismod. Sed placerat odio quis eros posuere vehicula. Pellentesque tincidunt iaculis leo nec lacinia. Nullam elit lectus, semper congue pulvinar ac, euismod eget dolor. In malesuada nisl id dolor tempor vulputate. Maecenas volutpat ornare sapien. Nam mi ligula, elementum nec ornare venenatis, consectetur eget neque.</p>
    <p>Lorem ipsum dolor sit amet, consectetur adipiscing elit. Morbi euismod sem eget neque consectetur a ultrices nunc porta. Pellentesque pharetra, lacus pharetra vehicula consequat, neque est luctus mauris, at lobortis mauris elit ac felis. Vestibulum blandit nulla at massa lacinia suscipit. Etiam aliquet nisl orci, at congue odio. Nunc vitae lectus mi. Suspendisse blandit consequat mi. Phasellus luctus lacinia lorem fermentum eleifend. Vivamus dignissim sollicitudin turpis et sagittis. Vivamus est dui, scelerisque eget sollicitudin at, lacinia ut ipsum. Aliquam quis sollicitudin arcu.</p>
    <h2>Lorem ipsum dolor sit amet</h2>
    <p>Sed volutpat tortor eget quam vulputate elementum. Quisque quis nulla et purus ornare luctus viverra quis est. In eu nunc et mi faucibus varius. Suspendisse et nulla urna. Nunc consequat arcu ipsum. Donec vel purus tortor. Donec ac urna arcu, ut scelerisque lacus. Morbi lacus enim, scelerisque sit amet tempus nec, pharetra et mauris. Quisque a lectus turpis. Vivamus velit nisi, vestibulum in viverra eu, sodales vestibulum quam. Maecenas neque lorem, malesuada et tempus nec, tempor nec nisl.</p>
    <p>In malesuada nisl id dolor tempor vulputate. Maecenas volutpat ornare sapien. Nam mi ligula, elementum nec ornare venenatis, consectetur eget neque. Vivamus velit nisi, vestibulum in viverra eu, sodales vestibulum quam. Maecenas neque lorem, malesuada et tempus nec, tempor nec nisl. Vivamus velit nisi, vestibulum in viverra eu, sodales vestibulum quam. Maecenas neque lorem, malesuada et tempus nec, tempor nec nisl.</p>
  </main>

  <footer class="page-footer">
    <div class="page-tab">pag. 2</div>
    <div class="footer-rule"></div>
  </footer>
</div>
</body>
</html>
```